Tallow Bodyweight Gym Website

We need a website design for our gym.

Tallow is the UAE's first calisthenics and parkour gym. The theme under which the gym revolves is that one does not require any machinery to workout as our bodies could be themselves the machinery. The gym is designed to be the more of a social hub rather than an "in-and-out" gym, where people come train, have fun, hang out and socialize for a few hours rather than just train for 60 minutes then leave. The gym is designed to be a big open space with lots of natural sunlight, natural wood and plants all over the place to create a natural and refreshing setting. We also use recycled material throughout the gym and recycle our waste as being green is part of our philosophy. We currently also have some of the world's top and most recognized calisthenics athletes working with us.

We would like our website to reflect all that as well as provide a simple, interactive and fun way for visitors to be able to get class and gym information, check out gym media and contact us for bookings.

Target Market(s)

Ages 15-35

Industry/Entity Type

Fitness

Coding

Coded - Design and coding required

Number of Pages Required

4 page

Font styles to use
Decorative

Colors
0792cd

Requirements
Must have
• Class descriptions
• Gym description
• Class schedules
• Trainer profiles
• Gym philosophy
• Contact Details
Nice to have
• A link to contact us directly for a free first trial class

```html
<!DOCTYPE html>
<html lang="en">
<head>
<meta charset="utf-8">
<title>Tallow Bodyweight Gym</title>
<link rel="stylesheet" href="https://fonts.googleapis.com/css2?family=Open+Sans:ital,wght@0,400;0,600;0,700;0,800;1,400;1,600&display=swap">
<style>
:root{
  --blue:#0792cd;
  --blue-light:#1ea6dc;
  --ink:#333;
  --muted:#777;
  --dark:#1b1b1b;
  --darker:#111;
  --panel:#f3f4f6;
  --white:#fff;
}
*{box-sizing:border-box;margin:0;padding:0}
html,body{width:1200px;height:2553px;overflow:hidden}
body{font-family:"Open Sans",Arial,sans-serif;color:var(--ink);background:var(--white);position:relative}
a{color:inherit;text-decoration:none}

.wordmark{font-weight:700;color:var(--ink);white-space:nowrap}

/* header */
.site-header{position:relative;height:102px;border-top:3px solid var(--blue)}
.site-header .wordmark{position:absolute;left:88px;top:14px;font-size:19px}
.call{position:absolute;right:80px;top:14px;font-size:12px;color:#444;display:flex;gap:8px;align-items:center}
.main-nav{position:absolute;left:285px;right:0;top:48px;height:54px;background:var(--blue);display:flex;align-items:center;padding-left:18px}
.main-nav a{color:var(--white);font-size:12px;font-weight:600;text-transform:uppercase;padding:0 12px;line-height:54px}
.main-nav a.active{background:#222;padding:0 18px;clip-path:polygon(10px 0,100% 0,100% 100%,0 100%)}

/* hero */
.hero{position:relative;height:463px;background:linear-gradient(180deg,#2b2f31,#3b3f40 60%,#232526)}
.hero h1{position:absolute;left:0;right:0;top:100px;text-align:center;font-size:80px;font-weight:800;color:var(--white);letter-spacing:1px;line-height:1.2}
.hero-sub{position:absolute;left:600px;top:198px;color:var(--blue-light);font-style:italic;font-size:14px}
.hero p{position:absolute;left:250px;right:250px;top:240px;text-align:center;color:#eee;font-size:12px;line-height:26px}
.btn-trial{position:absolute;left:475px;top:322px;width:250px;height:53px;border-radius:27px;background:var(--blue);color:var(--white);font-weight:700;font-size:15px;display:flex;align-items:center;justify-content:center;box-shadow:0 3px 0 #056e9a}
.dots{position:absolute;top:424px;left:0;right:0;display:flex;justify-content:center;gap:4px}
.dots span{width:14px;height:14px;border:2px solid #ddd;border-radius:50%}
.dots span.on{background:var(--blue)}

/* section titles */
.sec-title{text-align:center;font-size:24px;font-weight:700;color:#333;text-transform:uppercase}
.lead{text-align:center;font-size:12px;color:#666;line-height:27px}

.welcome{height:322px;padding-top:55px}
.welcome h3{text-align:center;color:var(--blue-light);font-size:19px;font-weight:400;margin:30px 0 6px}
.welcome .lead{width:730px;margin:0 auto}

/* about */
.about{height:412px;display:flex}
.about-photo{width:540px;background:linear-gradient(160deg,#3a3e42,#2a2d30);position:relative;color:var(--white);padding:85px 0 0 87px}
.about-photo h2{font-size:24px;font-weight:700}
.about-photo hr{border:0;height:2px;width:80px;background:var(--blue);margin:10px 0 14px}
.about-photo p{font-style:italic;font-size:12px;line-height:26px;color:#bbb;width:400px}
.btn-outline{display:inline-flex;margin-top:32px;border:2px solid var(--blue);border-radius:22px;padding:10px 16px;color:var(--blue-light);font-size:12px}
.features{flex:1;background:var(--panel);display:grid;grid-template-columns:1fr 1fr;padding:15px 0}
.feature{text-align:center;padding-top:10px}
.feature:nth-child(odd){border-right:1px solid #e2e2e2}
.feature:nth-child(-n+2){border-bottom:1px solid #e2e2e2}
.feature-icon{width:64px;height:60px;margin:0 auto;border-radius:50%;background:var(--blue)}
.feature h4{font-size:16px;font-weight:600;margin:12px 0 8px}
.feature p{font-size:12px;color:#777;line-height:22px;width:245px;margin:0 auto}

/* works */
.works{height:476px;padding-top:52px}
.works .lead{width:800px;margin:18px auto 0}
.cards{display:flex;gap:20px;margin:32px 0 0 87px}
.card{width:329px;height:245px;position:relative;background:linear-gradient(160deg,#66696b,#3a3c3e)}
.card.c2{background:linear-gradient(160deg,#8d9597,#4c5457)}
.card.c3{background:linear-gradient(160deg,#4a5d72,#2b3440)}
.card-tag{position:absolute;left:0;top:145px;background:var(--blue);color:var(--white);font-size:14px;font-weight:600;padding:7px 40px 7px 12px;clip-path:polygon(0 0,88% 0,100% 100%,0 100%)}
.card-link{position:absolute;left:0;top:182px;background:rgba(0,0,0,.75);color:var(--white);font-size:13px;padding:9px 12px;display:flex;gap:12px;align-items:center}

/* teams */
.teams{height:335px;background:var(--blue);position:relative;color:var(--white);padding-top:38px}
.teams .sec-title{color:var(--white)}
.teams h3{text-align:center;font-size:19px;font-weight:400;margin-top:10px}
.arrow{position:absolute;top:130px}
.avatar{position:absolute;left:231px;top:158px;width:120px;height:120px;border-radius:50%;border:4px solid var(--white);background:linear-gradient(160deg,#d8d4d0,#8d8782)}
.quote{position:absolute;left:390px;top:150px;width:560px;font-style:italic;font-size:12px;line-height:25px}
.quote strong{display:block;font-style:normal;font-weight:700;font-size:13px;margin-top:22px}
.quote small{font-size:11px}
.qmark{font-size:28px;font-weight:700;position:absolute}

/* partners */
.partners{height:133px;display:flex;align-items:center;justify-content:center;gap:52px;border-bottom:3px solid var(--blue)}
.partners .wordmark{font-size:22px;font-weight:600;color:#777}
.partners .chev{color:#aaa;font-size:22px}

/* footer */
.site-footer{height:245px;background:var(--dark);color:#ccc;position:relative;font-size:12px}
.site-footer .wordmark{position:absolute;left:87px;top:36px;color:#ddd;font-size:19px}
.f-about{position:absolute;left:87px;top:142px;width:245px;line-height:22px}
.f-col{position:absolute;top:40px}
.f-col h5{color:var(--blue-light);font-size:13px;font-weight:600;margin-bottom:14px;text-transform:uppercase}
.f-col li{list-style:none;line-height:23px;display:flex;gap:12px;align-items:flex-start}
.socials{display:flex;gap:10px;margin-top:20px}
.socials span{width:38px;height:38px;border-radius:50%;border:2px solid #ddd;display:flex;align-items:center;justify-content:center;font-size:9px;color:#eee}
.copyright{height:65px;background:var(--darker);color:#ddd;font-size:11px;text-align:center;line-height:65px}
</style>
</head>
<body>

<header class="site-header">
  <a class="wordmark" href="#">Tallow Bodyweight Gym</a>
  <div class="call">
    <svg width="14" height="12" viewBox="0 0 14 12"><path d="M1 4c0-3 12-3 12 0v1H10V3.5H4V5H1z M3 6h8l1 5H2z" fill="#0792cd"/></svg>
    CALL US L (000)-484-7720
  </div>
  <nav class="main-nav">
    <a class="active" href="#">Home</a>
    <a href="#">Class Descriptions</a>
    <a href="#">Gym Description</a>
    <a href="#">Class Schedules</a>
    <a href="#">Trainer Profiles</a>
    <a href="#">Gym Philosophy</a>
    <a href="#">Contact</a>
  </nav>
</header>

<section class="hero" role="img" aria-label="Gym interior with a plant wall and rows of dumbbells">
  <h1>TALLOW</h1>
  <div class="hero-sub">calisthenics &amp; Parkour Gym</div>
  <p>It is a long established fact that a reader will be distracted by the readable content of a page when looking at its layout. The point of , and a search for 'lorem ipsum' will uncover many web sites still in their infancy</p>
  <a class="btn-trial" href="#">FREE FIRST TRIAL CLASS</a>
  <div class="dots"><span></span><span></span><span class="on"></span><span></span><span></span></div>
</section>

<section class="welcome">
  <h2 class="sec-title">Welcome to Tallow</h2>
  <h3>TALLOW IS THE UAE'S FIRST CALISTHENICS AND PARKOUR GYM</h3>
  <p class="lead">It is a long established fact that a reader will be distracted by the readable content of a page when looking at its layout. The point of using Lorem Ipsum is that it has a more-or-less normal distribution of letters, as opposed to using Content here content here making it look like readable English. Many desktop publishing packages and web page editors now use Lorem Ipsum as their default model text, and a search for 'lorem ipsum' will uncover many web sites still in their infancy</p>
</section>

<section class="about">
  <div class="about-photo" role="img" aria-label="Dim gym hall with training rigs">
    <h2>ABOUT PARKOUR GYM</h2>
    <hr>
    <p>It is a long established fact that a reader will be distracted by the readable content of a page when looking at its layout. The point of using Lorem Ipsu m is that it has a more-or-less normal distribution of letters, cover many web sites still in their infancy</p>
    <a class="btn-outline" href="#">READ MORE INFO &nbsp;»</a>
  </div>
  <div class="features">
    <div class="feature"><div class="feature-icon" role="img" aria-label="Weightlifting icon"></div><h4>Contrary to popular</h4><p>long established fact that a reader will be distracted by the readable content of a page when looking at its layout.</p></div>
    <div class="feature"><div class="feature-icon" role="img" aria-label="Rowing icon"></div><h4>Contrary to popular</h4><p>long established fact that a reader will be distracted by the readable content of a page when looking at its layout.</p></div>
    <div class="feature"><div class="feature-icon" role="img" aria-label="Cycling stretch icon"></div><h4>Contrary to popular</h4><p>long established fact that a reader will be distracted by the readable content of a page when looking at its layout.</p></div>
    <div class="feature"><div class="feature-icon" role="img" aria-label="Handstand icon"></div><h4>Contrary to popular</h4><p>long established fact that a reader will be distracted by the readable content of a page when looking at its layout.</p></div>
  </div>
</section>

<section class="works">
  <h2 class="sec-title">Our Works</h2>
  <p class="lead">It is a long established fact that a reader will be distracted by the readable content of a page when looking at its layout. The point of , and a search for 'lorem ipsum' will uncover many web sites still in their infancy</p>
  <div class="cards">
    <div class="card" role="img" aria-label="Gym lounge with a green plant wall">
      <span class="card-tag">CLASS DESCRIPTIONS</span>
      <a class="card-link" href="#">Click Here For Read More Info <span>⊙</span></a>
    </div>
    <div class="card c2" role="img" aria-label="Open training floor with pull-up frame">
      <span class="card-tag">GYM DESCRIPTION</span>
      <a class="card-link" href="#">Click Here For Read More Info <span>⊙</span></a>
    </div>
    <div class="card c3" role="img" aria-label="Training rigs in a busy gym">
      <span class="card-tag">CLASS SCHEDULES</span>
      <a class="card-link" href="#">Click Here For Read More Info <span>⊙</span></a>
    </div>
  </div>
</section>

<section class="teams">
  <h2 class="sec-title">Our Teams</h2>
  <h3>TALLOW IS THE UAE'S FIRST CALISTHENICS AND PARKOUR GYM</h3>
  <svg class="arrow" style="left:48px" width="20" height="80" viewBox="0 0 20 80"><path d="M18 2 2 40l16 38" fill="none" stroke="#fff" stroke-width="1.5"/></svg>
  <svg class="arrow" style="right:48px" width="20" height="80" viewBox="0 0 20 80"><path d="M2 2l16 38L2 78" fill="none" stroke="#fff" stroke-width="1.5"/></svg>
  <div class="avatar" role="img" aria-label="Trainer portrait"></div>
  <div class="quote">
    <span class="qmark" style="left:-12px;top:-14px">“</span>
    <p>Lorem Ipsum is simply dummy text of the printing and typesetting industry. Lorem Ipsum has been the industry's standard dummy text ever since the 1500s, when an unknown printer took a galley of type and scrambled it to make a type specimen book...</p>
    <span class="qmark" style="right:-6px;top:54px">”</span>
    <strong>RAMI HADDAD</strong>
    <small>Posed on 25 Oct 2015</small>
  </div>
</section>

<section class="partners">
  <span class="chev">‹</span>
  <span class="wordmark">Soundwell</span>
  <span class="wordmark">Northgrid</span>
  <span class="wordmark">Snapleaf</span>
  <span class="wordmark">stockframe</span>
  <span class="wordmark">Tilebox</span>
  <span class="wordmark">Snapleaf</span>
  <span class="chev">›</span>
</section>

<footer class="site-footer">
  <a class="wordmark" href="#">Tallow Bodyweight Gym</a>
  <p class="f-about">It is a long established fact that a reader will be distracted by the readable content of a page when looking at its layout.</p>
  <div class="f-col" style="left:412px">
    <h5>Contact Us</h5>
    <ul>
      <li><span style="color:var(--blue)">☎</span>(000)-484-7720 (Phone)</li>
      <li><span style="color:var(--blue)">☎</span>(000)-484-7721 (Fax)</li>
      <li><span style="color:var(--blue)">✉</span><u>info@tallowgym.ae</u></li>
      <li><svg width="10" height="14" viewBox="0 0 10 14" style="margin-top:5px"><path d="M5 0a5 5 0 0 1 5 5c0 4-5 9-5 9S0 9 0 5a5 5 0 0 1 5-5z" fill="#0792cd"/><circle cx="5" cy="5" r="2" fill="#1b1b1b"/></svg><span style="line-height:16px;padding-top:4px"># 66 lorem Ipsum dummy Text<br>Lorem</span></li>
    </ul>
  </div>
  <div class="f-col" style="left:700px">
    <h5>Quick Links</h5>
    <ul>
      <li>Home</li><li>Class descriptions</li><li>Gym description</li><li>Class schedules</li><li>Trainer profiles</li><li>Gym philosophy</li><li>Contact</li>
    </ul>
  </div>
  <div class="f-col" style="left:885px;width:235px">
    <h5>Follow Us</h5>
    <p style="line-height:20px">It is a long established fact that a reader will be distracted by the readable content of a page when looking at its layout.</p>
    <div class="socials"><span>Kinda</span><span>Perch</span><span>Reelo</span><span>Netwo</span></div>
  </div>
</footer>
<div class="copyright">© COPY RIGHT2015 TALLOW. ALL RIGHTS RESERVED</div>

</body>
</html>
```